CREATE A BUSINESS CARD FOR A BOAT CLEANING SERVICE

WE ARE STARTING A NEW BOAT CLEANING BUSINESS. WE DIVE UNDERWATER TO CLEAN BOAT HULLS, JETTIES, UNDERWATER STRUCTURES ETC. WE ARE LOOKING FOR AN UPPERMARKET MODERN LOGO AND BUSINESS CARD AS ALOT OF OUR TARGET MARKET WILL BE HIGH END. YOU HAVE TO DESIGN A BUSINESS CARD AND LOGO SEPERATELY .
THE BUSINESS CARD DIMESNION MUST BE STANDARD SIZE.
The standard dimensions of a printed business card are 3.5 x 2 inches

Target Market(s)

UNDERWATER SERVICED

Industry/Entity Type

Business

Contact Information for Business Card

HALDEN UNDERWATER SERVICES

Font styles to use
Serif

Colors

Designer to choose colors to be used in the design.

Requirements
Must have
• HALDEN
Nice to have
• dark
Should not have
• more than 3 colors

```html
<!DOCTYPE html>
<html lang="en">
<head>
<meta charset="utf-8">
<title>Halden Underwater Service — Business Card</title>
<link rel="stylesheet" href="https://fonts.googleapis.com/css2?family=Jost:wght@400&family=Lato:wght@400&display=swap">
<style>
  :root {
    --page: #efefef;
    --card: #0f0f10;
    --blue: #1b5593;
    --white: #f1f1f1;
  }
  * { margin: 0; padding: 0; box-sizing: border-box; }
  html, body { width: 1200px; height: 900px; overflow: hidden; background: var(--page); }
  .stage { position: relative; width: 1200px; height: 900px; }

  .card {
    position: absolute; top: 150px; width: 343px; height: 600px;
    background: var(--card); color: var(--white);
    font-family: "Lato", sans-serif;
  }
  .card--front { left: 246px; }
  .card--back  { left: 611px; }

  .line {
    position: absolute; left: 0; width: 100%; text-align: center; white-space: nowrap;
  }

  .brand-name {
    font-family: "Jost", sans-serif; font-weight: 400; color: var(--blue);
    font-size: 30px; letter-spacing: 0.62em; text-indent: 0.62em; line-height: 1;
  }
  .brand-tag {
    font-family: "Jost", sans-serif; font-weight: 400; color: var(--white);
    font-size: 16px; letter-spacing: 0.28em; text-indent: 0.28em; line-height: 1;
  }

  .person-name {
    font-family: "Jost", sans-serif; color: var(--blue);
    font-size: 22px; letter-spacing: 0.1em; line-height: 1;
  }
  .person-role { font-size: 16px; line-height: 1; }
  .contact { font-size: 14px; line-height: 1; letter-spacing: 0.02em; }

  .pin { position: absolute; left: 157px; top: 404px; width: 29px; height: 29px; }

  .partners {
    position: absolute; top: 522px; left: 0; width: 100%;
    display: flex; justify-content: center; align-items: center; gap: 34px;
  }
  .partner-badge {
    width: 78px; height: 50px; border-radius: 50%;
    background: linear-gradient(160deg, #2f7fa8, #123c5c);
  }
  .partner-name {
    display: flex; align-items: center; gap: 6px;
    font-family: "Jost", sans-serif; font-size: 24px; color: var(--white); letter-spacing: 0.02em;
  }
  .partner-dot { width: 22px; height: 22px; border-radius: 50%; background: var(--blue); }

  .site { font-size: 15px; line-height: 1; letter-spacing: 0.02em; }
  .site .accent { color: var(--blue); }
</style>
</head>
<body>
<main class="stage">

  <section class="card card--front" aria-label="Business card front">
    <div class="line brand-name" style="top:131px">HALDEN</div>
    <div class="line brand-tag" style="top:167px">UNDERWATER SERVICE</div>

    <div class="line person-name" style="top:251px">TOM VELLER</div>
    <div class="line person-role" style="top:278px">CEO / Founder</div>

    <div class="line contact" style="top:325px">555-014-2210 | 555-014-2276</div>
    <div class="line contact" style="top:344px">info@haldenunderwaterservice.com</div>
    <div class="line contact" style="top:364px">www.haldenunderwaterservice.com</div>

    <svg class="pin" viewBox="0 0 29 29" aria-hidden="true">
      <circle cx="14.5" cy="14.5" r="14.5" fill="var(--blue)"/>
      <path d="M14.5 7.5a5 5 0 0 0-5 5c0 3.7 5 9 5 9s5-5.3 5-9a5 5 0 0 0-5-5z" fill="var(--white)"/>
      <circle cx="14.5" cy="12.5" r="1.8" fill="var(--blue)"/>
    </svg>

    <div class="line contact" style="top:443px">Kadestraat 8 4811XZ, Suite</div>
    <div class="line contact" style="top:463px">-200, Lindwater, The Netherlands</div>

    <div class="partners">
      <div class="partner-badge" role="img" aria-label="Partner badge"></div>
      <div class="partner-name"><span class="partner-dot"></span>HALDEN</div>
    </div>
  </section>

  <section class="card card--back" aria-label="Business card back">
    <div class="line brand-name" style="top:318px">HALDEN</div>
    <div class="line brand-tag" style="top:353px">UNDERWATER SERVICE</div>
    <div class="line site" style="top:531px">wwww.<span class="accent">haldenunderwaterservice</span>.com</div>
  </section>

</main>
</body>
</html>
```